Stationary Set and Logo Update **PAYMENT GUARANTEED**

Stationery Design and Logo Update

About Us

Trindex Supply is a wholesale distributor of OEM [original brand] and compatible [generic brand] parts and supplies for use in copiers, faxes, printers, and multi-function machines. In plain English…we sell all the parts and supplies [such as toner] that make up any office equipment which outputs an image on paper.

Trindex was the 1st distributor to develop and sell a generic brand copier part in the United States. We have been in business since 1972 [nearly 40 years]. Our tagline is "The Steady Choice," as in our company was the first alternative product that copier dealers had to buying original brand copier parts. Trindex is known for offering reliable and cost-effective OEM and compatible products.

Project

We require a fresh, modern and corporate identity. Please submit a stationary package inclusive of a double-sided business card (2" x 3.5"), letterhead (8.5'x11"), and standard #10 envelope (4-1/8” x 9-1/2). You may use our current logo or preferably your take on an updated one. If an attempt is made in updating the logo #004D8E or a similar hue should be used as the primary color.

The design should be clean, simple, modern and professional and make an immediate impact.

Target Market(s)

Copier and printer dealers who lease and service imaging equipment in the United States and Latin America.

Industry/Entity Type

Business

Requirements
Must have
• Simple, clean, modern and professional. Please use #004D8E or a similar hue as the primary color. Letterhead must accommate (2) addresses. We have 2 locations.
Nice to have
• A simple, modern update to our current logo. https://assets.mailvorbo.example/fs030/5520384417702/img/418.jpg
Should not have
• More than (2) colors on logo.

```html
<!DOCTYPE html>
<html lang="en">
<head>
<meta charset="utf-8">
<title>Trindex Supply Letterhead</title>
<link href="https://fonts.googleapis.com/css2?family=Arimo:wght@400;700&display=swap" rel="stylesheet">
<style>
:root{
  --brand:#1d4f9c;
  --ink:#1f2a3a;
  --paper:#ffffff;
  --rule:#ffffff;
}
*{box-sizing:border-box;margin:0;padding:0}
html,body{width:849px;height:1200px;overflow:hidden;background:var(--paper)}
body{font-family:"Arimo",Arial,sans-serif;color:var(--ink);position:relative}
.top-band{position:absolute;left:0;top:0;width:849px;height:10px;background:var(--brand)}
.brand{position:absolute;left:44px;top:86px;display:flex;align-items:center;gap:10px}
.brand-dot{width:40px;height:40px;border-radius:50%;background:var(--brand)}
.brand-name{font-size:46px;font-weight:700;color:var(--brand);letter-spacing:-0.5px}
.recipient{position:absolute;left:56px;top:240px;font-size:14.5px;font-weight:700;line-height:19px}
.letter{position:absolute;left:56px;top:428px;width:742px;font-size:14.5px;line-height:17.5px}
.letter p{margin-bottom:17.5px}
.footer{position:absolute;left:0;top:1022px;width:849px;height:178px;background:var(--brand);color:#fff;display:flex;padding:28px 0 0 56px;font-size:14px;line-height:18.5px}
.office{padding-right:18px}
.office + .office{border-left:1.5px solid var(--rule);padding-left:16px}
.office.main{width:268px}
.office.west{width:278px}
</style>
</head>
<body>
<div class="top-band"></div>

<header class="brand">
  <span class="brand-dot"></span>
  <span class="brand-name">Trindex</span>
</header>

<address class="recipient" style="font-style:normal">
  To, Ravi Deshmane<br>Talegaon, Nashik<br>India.
</address>

<main class="letter">
  <p>Dear Client,</p>
  <p>Lorem ipsum dolor sit amet, consectetuer adipiscing elit. Praesent mattis eros a tellus. Quisque leo tortor, commodo id, dapibus et, lacinia et, justo. Ut urna sapien, dictum eu, cursus vel, consectetuer tincidunt, eros. Etiam in libero. Etiam tempor. Maecenas ligula felis, commodo eget, scelerisque id, suscipit nec, odio. Vivamus commodo, magna in mollis feugiat, felis nisl dapibus dolor, eu blandit orci nulla in orci. Cras felis ipsum, mollis at, semper et, tincidunt id, ipsum. Ut consectetuer elit nec elit. Cras luctus molestie ligula. In gravida tempor nunc.</p>
  <p>Curabitur nisl ligula, pulvinar et, volutpat non, porta a, ipsum. Donec tristique ante at est. Pellentesque volutpat est non diam. Aenean vel velit. Suspendisse facilisis nisl et massa. Mauris nec erat. Pellentesque luctus arcu ut dui. Proin suscipit lorem id augue. Maecenas eget ipsum nec orci convallis viverra. Suspendisse potenti. Donec sed enim. Ut et turpis. Ut mattis enim nec nisl. Ut quam. Pellentesque lobortis vehicula risus.</p>
  <p>Etiam massa erat, tempor et, elementum fringilla, pellentesque ac, odio. Cras sed felis. Aliquam erat volutpat. Etiam tristique. Donec pellentesque, nulla semper adipiscing faucibus, nibh augue semper sapien, eget feugiat dui massa et urna. Nullam ac arcu. Quisque interdum. Morbi tristique sagittis arcu. Phasellus euismod ante eget risus. Nam convallis rutrum augue. Pellentesque placerat ultrices tellus.</p>
  <p>Ut lacinia. Sed aliquet diam at odio. Nunc ultrices pretium urna. Sed risus velit, nonummy eget, suscipit at, sagittis in, tortor. Quisque risus. Duis porta. Nunc blandit, augue et nonummy ultrices, lacus justo tincidunt nibh, eu vestibulum turpis metus iaculis ipsum. Morbi neque. Quisque augue. Etiam eleifend rhoncus metus. Aliquam auctor libero non nisi.</p>
  <p>Your Sincerely,<br>your name</p>
</main>

<footer class="footer">
  <div class="office main">
    Corporate Office<br>
    2280 Harbor Crest Drive<br>
    Coral Bay, FL 33019<br>
    Toll Free: 800.555.0142<br>
    Local: 954.555.0187<br>
    Fax: 954.555.0193
  </div>
  <div class="office west">
    Trindex West<br>
    Western Distribution Center<br>
    Sierra Gate Industrial Park #4<br>
    4417 Meridian Way. Carson, NV 89502<br>
    Toll Free: 800.555.0168<br>
    Fax: 775.555.0124
  </div>
  <div class="office web">
    for more information visit us -<br>
    www.trindexnet.example<br>
    or call us toll free -<br>
    800.555.0168
  </div>
</footer>
</body>
</html>
```